Business card for apparel company. Specializing in fishing and boating performance wear. Main company name is Marlow Pelican Company, LLC brand name for apparel is TIDEWAKE. See website www.TidewakeBayline.com I will attach some logos to consider.

```html
<!DOCTYPE html>
<html lang="en">
<head>
<meta charset="utf-8">
<title>Tidewake Business Card</title>
<link href="https://fonts.googleapis.com/css2?family=Chakra+Petch:wght@500;700&display=swap" rel="stylesheet">
<style>
  :root {
    --page: #f2f3f5;
    --navy: #181b33;
    --white: #ffffff;
    --silver: #dfe5ec;
    --sky: #1eaaf0;
    --blue: #0a8ae0;
    --ink: #5b5f66;
    --faint: #eef0f2;
  }
  * { box-sizing: border-box; margin: 0; padding: 0; }
  html, body { width: 1200px; height: 1000px; overflow: hidden; }
  body {
    background: var(--page);
    font-family: "Chakra Petch", sans-serif;
    position: relative;
  }
  .card {
    position: absolute;
    left: 293px;
    width: 615px;
    height: 351px;
    border-radius: 32px;
    overflow: hidden;
  }
  .card-front { top: 108px; background: var(--navy); }
  .card-back { top: 510px; background: var(--white); box-shadow: 0 0 0 1px #e3e5e8; }

  .front-mark {
    position: absolute; left: 262px; top: 82px;
    width: 90px; height: 90px; border-radius: 50%;
    background: var(--sky);
  }
  .front-name {
    position: absolute; left: 0; right: 0; top: 196px;
    text-align: center; font-weight: 700; font-size: 54px;
    letter-spacing: 2px; color: var(--silver); line-height: 1;
  }
  .front-place {
    position: absolute; left: 176px; width: 264px; top: 266px;
    display: flex; align-items: center; gap: 8px;
    color: var(--white); font-weight: 500; font-size: 14px; letter-spacing: 1.5px;
  }
  .front-place .rule { flex: 1; height: 3px; background: var(--sky); border-radius: 2px; }

  .back-name {
    position: absolute; left: 50px; width: 270px; top: 98px;
    text-align: center; font-weight: 700; font-size: 38px;
    letter-spacing: 1px; color: var(--blue); line-height: 1;
  }
  .back-company {
    position: absolute; left: 40px; width: 290px; top: 162px;
    text-align: center; font-weight: 700; font-size: 15px;
    letter-spacing: 1.5px; color: var(--sky); text-transform: uppercase;
  }
  .back-rule {
    position: absolute; left: 144px; top: 190px;
    width: 83px; height: 3px; background: var(--sky);
  }
  .contact {
    position: absolute; left: 30px; width: 310px; top: 206px;
    list-style: none; text-align: center;
    font-weight: 500; font-size: 15px; letter-spacing: 1px;
    color: var(--ink); text-transform: uppercase; line-height: 21px;
  }
  .contact svg { width: 14px; height: 14px; vertical-align: -2px; margin-right: 5px; fill: var(--sky); }
  .stamp {
    position: absolute; left: 356px; top: 20px;
    width: 330px; height: 330px; border-radius: 50%;
    background: radial-gradient(circle, var(--faint) 0 55%, #f6f7f8 56% 100%);
  }
</style>
</head>
<body>
  <section class="card card-front">
    <div class="front-mark"></div>
    <div class="front-name">TIDEWAKE</div>
    <div class="front-place"><span class="rule"></span><span>BAYLINE, FL</span><span class="rule"></span></div>
  </section>

  <section class="card card-back">
    <div class="stamp" role="img" aria-label="Faint authentic-original brand stamp decoration"></div>
    <div class="back-name">TIDEWAKE</div>
    <div class="back-company">Marlow Pelican Company, LLC</div>
    <div class="back-rule"></div>
    <ul class="contact">
      <li><svg viewBox="0 0 24 24"><path d="M6.6 10.8a15 15 0 0 0 6.6 6.6l2.2-2.2c.3-.3.7-.4 1-.2 1.1.4 2.3.6 3.6.6.6 0 1 .4 1 1V20c0 .6-.4 1-1 1A17 17 0 0 1 3 4c0-.6.4-1 1-1h3.5c.6 0 1 .4 1 1 0 1.3.2 2.5.6 3.6.1.3 0 .7-.2 1z"/></svg>012-345-678</li>
      <li><svg viewBox="0 0 24 24"><path d="M2 5h20v14H2z M2 5l10 8 10-8" /></svg>info@marlowpelicanco.com</li>
      <li><svg viewBox="0 0 24 24"><path d="M12 2a10 10 0 1 0 0 20 10 10 0 0 0 0-20zm6.9 6h-3a15 15 0 0 0-1.3-3.9A8 8 0 0 1 18.9 8zM12 4c.8 1.2 1.5 2.5 1.9 4h-3.8c.4-1.5 1.1-2.8 1.9-4zM4.3 14a8 8 0 0 1 0-4h3.4a16 16 0 0 0 0 4zm.8 2h3a15 15 0 0 0 1.3 3.9A8 8 0 0 1 5.1 16zm3-8h-3a8 8 0 0 1 4.3-3.9C8.8 5.3 8.4 6.6 8.1 8zM12 20c-.8-1.2-1.5-2.5-1.9-4h3.8c-.4 1.5-1.1 2.8-1.9 4zm2.3-6H9.7a14 14 0 0 1 0-4h4.6a14 14 0 0 1 0 4zm.3 5.9c.6-1.2 1-2.5 1.3-3.9h3a8 8 0 0 1-4.3 3.9zm1.7-5.9a16 16 0 0 0 0-4h3.4a8 8 0 0 1 0 4z"/></svg>TidewakeBayline.com</li>
    </ul>
  </section>
</body>
</html>
```